KVT Social Media Graphics (Square)

Use the following images and headlines to create 7 individual social media graphics (square size); You can mix and match the text that's there to create different social media graphics. Note: each graphic should have one of the pictures of the bottle on it and/or one of the images with a person on it (pics attached to the brief)

Target Market(s)

women and men who are overweight looking for fast, healthy weight loss

Industry/Entity Type

health and wellness

Colors
0054AA
0677BA
7BADD7
CADEEF
E8F1F8

Requirements
Must have
• Use color scheme that's complimentary to the blood sugar bottle
Nice to have
• the text provided in the WORD document

```html
<!DOCTYPE html>
<html lang="en">
<head>
<meta charset="utf-8">
<title>KVT – Prescription-Free Weight Loss</title>
<link href="https://fonts.googleapis.com/css2?family=Archivo:wght@300;500;700;800&display=swap" rel="stylesheet">
<style>
  :root {
    --navy: #342a7b;
    --indigo: #35309a;
    --royal: #3d4fb8;
    --sky: #4a82dc;
    --podium: #4b8ae3;
    --podium-dark: #3d68c8;
    --podium-light: #8fc8f7;
    --floor: #342a7b;
    --white: #ffffff;
    --pill-text: #35307f;
  }
  html, body {
    margin: 0;
    padding: 0;
    width: 1200px;
    height: 1200px;
    overflow: hidden;
    background: var(--white);
  }
  .ad {
    position: relative;
    width: 1200px;
    height: 1200px;
    overflow: hidden;
    font-family: "Archivo", Arial, sans-serif;
    color: var(--white);
    background: linear-gradient(180deg, var(--navy) 0%, var(--indigo) 35%, var(--royal) 55%, var(--sky) 71%);
  }
  .ad__art {
    position: absolute;
    inset: 0;
  }
  .eyebrow {
    position: absolute;
    top: 100px;
    left: 0;
    width: 1190px;
    text-align: center;
    margin: 0;
    font-weight: 500;
    font-size: 40px;
    letter-spacing: 3px;
  }
  .headline {
    position: absolute;
    top: 186px;
    left: 0;
    width: 1204px;
    text-align: center;
    margin: 0;
    font-size: 116px;
    line-height: 1;
    letter-spacing: -6px;
  }
  .headline__light { font-weight: 300; }
  .headline__bold { font-weight: 800; letter-spacing: -3px; }
  .callout {
    position: absolute;
    margin: 0;
    font-weight: 700;
    font-size: 28px;
    line-height: 28px;
    text-transform: uppercase;
  }
  .callout--left { right: 846px; top: 600px; text-align: right; }
  .callout--right { left: 850px; top: 722px; text-align: left; }
  .brand-pill {
    position: absolute;
    left: 368px;
    top: 1095px;
    width: 463px;
    height: 62px;
    border-radius: 31px;
    background: var(--white);
    color: var(--pill-text);
    display: flex;
    align-items: center;
    justify-content: center;
    font-weight: 800;
    font-size: 38px;
    letter-spacing: -1px;
  }
</style>
</head>
<body>
<main class="ad">
  <svg class="ad__art" width="1200" height="1200" viewBox="0 0 1200 1200">
    <defs>
      <radialGradient id="dotFade" cx="50%" cy="50%" r="50%">
        <stop offset="0" stop-color="#5b8fe0" stop-opacity="0.9"/>
        <stop offset="1" stop-color="#5b8fe0" stop-opacity="0.35"/>
      </radialGradient>
      <linearGradient id="podiumSide" x1="0" x2="1">
        <stop offset="0" stop-color="var(--podium-dark)"/>
        <stop offset="0.5" stop-color="var(--podium)"/>
        <stop offset="1" stop-color="var(--podium-dark)"/>
      </linearGradient>
      <radialGradient id="podiumTop" cx="50%" cy="30%" r="70%">
        <stop offset="0" stop-color="var(--podium-light)"/>
        <stop offset="1" stop-color="var(--podium)"/>
      </radialGradient>
      <linearGradient id="photoFill" x1="0" y1="0" x2="0" y2="1">
        <stop offset="0" stop-color="#f2f3f7"/>
        <stop offset="1" stop-color="#c9d3ea"/>
      </linearGradient>
      <radialGradient id="glow" cx="50%" cy="50%" r="50%">
        <stop offset="0" stop-color="#ffffff" stop-opacity="0.95"/>
        <stop offset="1" stop-color="#ffffff" stop-opacity="0"/>
      </radialGradient>
      <path id="sparkle" d="M0 -32 C3 -6 6 -3 32 0 C6 3 3 6 0 32 C-3 6 -6 3 -32 0 C-6 -3 -3 -6 0 -32Z"/>
    </defs>

    <!-- floor band -->
    <rect class="floor" x="0" y="853" width="1200" height="347" fill="var(--floor)"/>

    <!-- decorative dotted discs -->
    <circle role="img" aria-label="Decorative dotted circle pattern" cx="137" cy="348" r="80" fill="url(#dotFade)" opacity="0.7"/>
    <circle role="img" aria-label="Decorative dotted circle pattern" cx="1092" cy="531" r="115" fill="url(#dotFade)" opacity="0.45"/>

    <!-- headline rule -->
    <path d="M300 160 Q600 154 897 158 Q600 164 300 160Z" fill="var(--white)"/>
    <use href="#sparkle" transform="translate(330 160) scale(0.75)" fill="var(--white)"/>

    <!-- podium -->
    <rect x="135" y="1072" width="930" height="84" fill="url(#podiumSide)"/>
    <ellipse cx="600" cy="1156" rx="465" ry="28" fill="url(#podiumSide)"/>
    <ellipse cx="600" cy="1072" rx="465" ry="45" fill="#5b95e8" stroke="#a9dcfb" stroke-width="1.5"/>
    <rect x="258" y="959" width="684" height="103" fill="url(#podiumSide)"/>
    <ellipse cx="600" cy="1062" rx="342" ry="24" fill="url(#podiumSide)"/>
    <ellipse cx="600" cy="959" rx="342" ry="36" fill="url(#podiumTop)" stroke="#b7e6fb" stroke-width="1.5"/>

    <!-- callout lines -->
    <g fill="none" stroke="var(--white)" stroke-width="2.5">
      <polyline points="490,512 372,512 372,727 455,727"/>
      <polyline points="773,650 829,650 829,865 742,865"/>
    </g>

    <!-- product photo area -->
    <rect class="product-photo" role="img" aria-label="Product photo: supplement bottle of Glyco Balance capsules, tilted on the podium"
          x="505" y="285" width="220" height="665" rx="30" fill="url(#photoFill)" transform="rotate(9 615 617)"/>
    <circle cx="793" cy="348" r="90" fill="url(#glow)"/>

    <!-- sparkles -->
    <use href="#sparkle" transform="translate(372 512) scale(1.05)" fill="var(--white)"/>
    <use href="#sparkle" transform="translate(897 491) scale(0.72)" fill="var(--white)"/>
    <use href="#sparkle" transform="translate(831 865) scale(0.6)" fill="var(--white)"/>
    <use href="#sparkle" transform="translate(1093 935) scale(0.72)" fill="var(--white)"/>
  </svg>

  <p class="eyebrow">PRESCRIPTION-FREE</p>
  <h1 class="headline"><span class="headline__light">WEIGHT</span> <span class="headline__bold">LOSS</span></h1>

  <p class="callout callout--left">Increase<br>GLP-1 Levels</p>
  <p class="callout callout--right">Reduce cravings<br>for sugar<br>and carbs</p>

  <div class="brand-pill">GLYCO BALANCE</div>
</main>
</body>
</html>
```